International Trade Consulting Firm Seeks Quality Newsletter Design

Our company provides consulting services to Pinnacle 300 type companies. We compete with the largest consulting companies in the world. However, we have the highest level of expertise in the industry and need to look the most professional and high end. We have very relevant and important information to provide our customers about their compliance and projects. We will have the winning design coded to be an e-newsletter, so it needs to be one page. We want to keep our company colors and logo design in the newsletter, they are attached. We DO NOT want it to look like a mini-version of our website. We want a fresh look to this marketing piece. Newsletter will need to include title, possible sub-heading, space for a feature story, 2 other stories included, and space on either the left or right for short cuts, links or highlights of other articles. Contents/'In this issue' section, about us or branding area, section for relevant links, etc...
Target Market(s)
Pinnacle 300 companies, High-level management
Industry/Entity Type
Marketing

```html
<!DOCTYPE html>
<html lang="en">
<head>
<meta charset="utf-8">
<title>Harborline Trade Partners — Newsletter Issue 01</title>
<link rel="stylesheet" href="https://fonts.googleapis.com/css2?family=Open+Sans:wght@300;400;600;700&family=Arimo:ital,wght@0,400;0,700;1,700&display=swap">
<style>
  :root {
    --black: #000000;
    --ink: #111111;
    --green: #4b9d3c;
    --gold: #e9d48c;
    --bar-gold: #f3d46a;
    --grey-text: #555555;
    --rule: #d9d9d9;
    --ad-fill: #eeeeee;
    --ad-border: #dcdcdc;
    --ad-text: #c4c4c4;
    --white: #ffffff;
  }
  * { box-sizing: border-box; margin: 0; padding: 0; }
  html, body { width: 1200px; height: 3046px; overflow: hidden; background: var(--white); }
  body { position: relative; font-family: "Arimo", Arial, sans-serif; color: var(--ink); }

  /* Header */
  .masthead { position: absolute; left: 0; top: 0; width: 1200px; height: 181px; background: var(--black); }
  .masthead-rule { position: absolute; left: 0; top: 181px; width: 1200px; height: 6px;
    background: linear-gradient(to bottom, var(--green) 0 3px, var(--gold) 3px 6px); }
  .brand { position: absolute; left: 28px; top: 50px; display: flex; align-items: center; gap: 16px; }
  .brand-mark { width: 58px; height: 58px; background: var(--green); }
  .brand-name { font-family: "Open Sans", sans-serif; font-weight: 700; font-size: 40px; line-height: 1.05; color: var(--green); letter-spacing: 1px; }
  .issue { position: absolute; right: 32px; top: 44px; text-align: right; color: var(--white); font-family: "Open Sans", sans-serif; }
  .issue-label { font-size: 17px; font-weight: 400; }
  .issue-number { font-size: 50px; font-weight: 600; line-height: 1.05; }
  .issue-date { font-size: 17px; font-weight: 700; font-style: italic; font-family: "Arimo", Arial, sans-serif; }

  /* Main column */
  .main { position: absolute; left: 28px; top: 0; width: 849px; }
  .welcome-title { position: absolute; top: 244px; font-family: "Open Sans", sans-serif; font-weight: 300; font-size: 37px; color: var(--gold); }
  .body-text { font-size: 24.5px; line-height: 34.5px; color: var(--ink); }
  .welcome-text { position: absolute; top: 296px; width: 849px; }

  .story { position: absolute; left: 0; width: 849px; }
  .story-bar { position: relative; height: 57px; background: var(--black); color: var(--bar-gold);
    font-family: "Open Sans", sans-serif; font-size: 19px; line-height: 57px; padding-left: 20px; text-transform: uppercase; }
  .story-bar::after { content: ""; position: absolute; left: 20px; bottom: -12px; border-left: 8px solid transparent; border-right: 8px solid transparent; border-top: 12px solid var(--black); }
  .feature-photo { margin-top: 29px; height: 342px; border-radius: 8px;
    background: radial-gradient(ellipse at 40% 50%, #d9d9d9 0%, #9a9a9a 55%, #3e3e3e 100%); }
  .story-title { font-family: "Arimo", Arial, sans-serif; font-weight: 700; font-style: italic; font-size: 37px; color: var(--green); line-height: 1; }
  .story--feature .story-title { margin-top: 26px; }
  .story--feature .body-text { margin-top: 12px; }
  .story--other .story-title { margin-top: 30px; }
  .story-inline-photo { float: right; width: 335px; height: 238px; margin: 2px 0 6px 24px; border-radius: 6px; }
  .photo-meeting { background: linear-gradient(135deg, #c9cdd3 0%, #6b6f78 50%, #2b2f3a 100%); }
  .photo-growth { background: linear-gradient(160deg, #f4f6f8 0%, #d7dde3 45%, #2f7fc2 80%, #f09a1e 100%); }
  .story--other .story-body { margin-top: 18px; }
  .read-more { clear: both; display: flex; justify-content: flex-end; padding-top: 10px; }
  .read-more a { position: relative; display: block; width: 230px; text-align: right; padding-bottom: 8px;
    font-family: "Open Sans", sans-serif; font-weight: 700; font-size: 19px; color: var(--green); text-decoration: none; }
  .read-more a::after { content: ""; position: absolute; right: 0; bottom: 0; width: 230px; height: 3px; background: linear-gradient(to right, rgba(75,157,60,0), var(--green)); }

  /* Column divider */
  .column-rule { position: absolute; left: 905px; top: 222px; width: 2px; height: 2398px; background: var(--rule); }

  /* Sidebar */
  .sidebar { position: absolute; left: 934px; top: 0; width: 238px; }
  .side-heading { position: absolute; left: 0; width: 238px; font-family: "Open Sans", sans-serif; font-weight: 700; font-size: 21px; color: var(--black); padding-bottom: 6px; }
  .side-heading::after { content: ""; position: absolute; left: 0; bottom: 0; width: 238px; height: 3px; background: linear-gradient(to right, var(--black) 55%, rgba(0,0,0,0)); }
  .side-list { position: absolute; left: 0; list-style: none; font-size: 22px; line-height: 34.4px; }
  .side-list a { color: var(--green); text-decoration: none; }
  .side-list--issue { font-weight: 700; }
  .who-photo { position: absolute; left: 0; top: 790px; width: 238px; height: 144px; border-radius: 4px;
    background: linear-gradient(120deg, #6f5a3a 0%, #a8a07a 45%, #9cc27a 75%, #4d6b38 100%); }
  .who-text { position: absolute; left: 0; top: 944px; width: 238px; font-size: 20px; line-height: 28.6px; color: var(--grey-text); }
  .social { position: absolute; left: 0; top: 1305px; display: flex; gap: 4px; }
  .social span { width: 35px; height: 35px; display: block; }
  .ad { position: absolute; left: 0; width: 238px; height: 238px; background: var(--ad-fill); border: 5px solid var(--ad-border);
    display: flex; flex-direction: column; align-items: center; justify-content: center;
    font-family: "Open Sans", sans-serif; font-weight: 600; font-size: 16px; line-height: 24px; color: var(--ad-text); text-align: center; }

  /* Footer */
  .footer-wave { position: absolute; left: 0; top: 2630px; width: 1200px; height: 90px; }
  .footer { position: absolute; left: 0; top: 2700px; width: 1200px; height: 346px; background: var(--black); text-align: center; color: var(--white); }
  .footer-brand { position: absolute; left: 0; right: 0; top: 40px; display: flex; justify-content: center; align-items: center; gap: 14px; }
  .footer-brand .brand-mark { width: 44px; height: 44px; background: #8a8a8a; }
  .footer-brand .brand-name { font-size: 32px; color: #8a8a8a; }
  .footer-name { position: absolute; left: 0; right: 0; top: 146px; font-family: "Open Sans", sans-serif; font-weight: 700; font-size: 24px; }
  .footer-line { position: absolute; left: 0; right: 0; font-family: "Open Sans", sans-serif; font-size: 18px; display: flex; justify-content: center; align-items: center; gap: 10px; }
  .footer-address { top: 187px; }
  .footer-contact { top: 226px; }
  .footer-contact a { color: var(--green); text-decoration: none; }
  .footer-contact .sep { margin: 0 12px; }
  .footer-line svg { width: 18px; height: 18px; fill: var(--white); }
  .copyright { position: absolute; left: 0; right: 0; top: 264px; font-size: 16px; font-style: italic; color: #8c8c8c; }
</style>
</head>
<body>

<header class="masthead">
  <div class="brand">
    <span class="brand-mark"></span>
    <span class="brand-name">HARBORLINE<br>TRADE PARTNERS</span>
  </div>
  <div class="issue">
    <div class="issue-label">ISSUE</div>
    <div class="issue-number">01</div>
    <div class="issue-date">May 30, 2014</div>
  </div>
</header>
<div class="masthead-rule"></div>

<main class="main">
  <h1 class="welcome-title">WELCOME</h1>
  <p class="body-text welcome-text">Lorem ipsum dolor sit amet, consectetur adipiscing elit. In vitae sem nec nisl commodo scelerisque non vel libero. Maecenas accumsan volutpat magna, sit ame pharetra eros tincidunt quis. Proin sed lacus id quam dignissim convallis. Phasellus interdum turpis a rhoncus consequat in sed massa leo port titor, luctus quam nec, tincidunt magna interdum vestibulum risus sit.</p>

  <article class="story story--feature" style="top:568px">
    <div class="story-bar">Featured Story</div>
    <div class="feature-photo" role="img" aria-label="Hand drawing a success diagram with arrows labelled team, planning, innovation and idea"></div>
    <h2 class="story-title">Featured Story Title</h2>
    <p class="body-text">Lorem ipsum dolor sit amet, consectetur adipiscing elit. In vitae sem nec nisl commodo scelerisque non vel libero. Maecenas accumsan volutpat magna, sit ame pharetra eros tincidunt quis. Proin sed lacus id quam dignissim convallis. Phasellus interdum turpis a rhoncus consequat. In sed massa porttitor, auctor turpis sit amet, egestas metus. Morbi eu lacus felis. Nunc at leo port titor, luctus quam nec, tincidunt magna interdum vestibulum risus sit.</p>
    <div class="read-more"><a href="#">READ MORE</a></div>
  </article>

  <article class="story story--other" style="top:1437px">
    <div class="story-bar">Other Story 1</div>
    <h2 class="story-title">Other Story 1 Title</h2>
    <div class="story-body body-text">
      <div class="story-inline-photo photo-meeting" role="img" aria-label="Business people shaking hands at a meeting table"></div>
      Nulla in viverra risus. Nullam lectus ante, laoreet nec enim sed, vehicula suscipit felis. Ut tristique viverra justo sit amet venenatis. Vestibulum congue, ante ac tempus scelerisque, felis lorem sollicitudin arcu, vel laoreet diam velit id sapien. Proin a eros nibh. Aenean sodales sagittis tellus, et congue odio. In semper dictum nisi, eget facilisis arcu interdum sed. Mauris purus nibh, pellentesque eu viverra orquent prhoncus, volutpat ac tellus.
    </div>
    <div class="read-more"><a href="#">READ MORE</a></div>
  </article>

  <article class="story story--other" style="top:2056px">
    <div class="story-bar">Other Story 2</div>
    <h2 class="story-title">Other Story 2 Title</h2>
    <div class="story-body body-text">
      <div class="story-inline-photo photo-growth" role="img" aria-label="Rising blue bar graph with an orange growth arrow"></div>
      Curabitur pulvinar enim non tempor rutrum. Fusce nulla neque, sagittis ut sagittis id, eleifend a mauris. Etiam sem mi, tincidunt eget tempus in, porttitor quis tortor. Nam auctor vel massa vitae ultrices. Vestibulum aliquam commodo risus nec congue. Etiam faucibus consectetur tortor, vel auctor diam dignissim sit amet. Integer quis justo rutrum, ullamcorper erat nec, rhoncus dolor. Sed posuere, tortor ut scelerisque ornare, diam purus scelerisque.
    </div>
    <div class="read-more"><a href="#">READ MORE</a></div>
  </article>
</main>

<div class="column-rule"></div>

<aside class="sidebar">
  <h3 class="side-heading" style="top:244px">IN THIS ISSUE</h3>
  <ul class="side-list side-list--issue" style="top:290px">
    <li><a href="#">A Feature Story</a></li>
    <li><a href="#">Other Story 1</a></li>
    <li><a href="#">Other Story 2</a></li>
  </ul>

  <h3 class="side-heading" style="top:439px">QUICK LINKS</h3>
  <ul class="side-list" style="top:484px">
    <li><a href="#">harborlinetrade.com</a></li>
    <li><a href="#">About Us</a></li>
    <li><a href="#">Services</a></li>
    <li><a href="#">Video &amp; News</a></li>
    <li><a href="#">Career</a></li>
    <li><a href="#">Contact us</a></li>
  </ul>

  <h3 class="side-heading" style="top:735px">WHO WE ARE</h3>
  <div class="who-photo" role="img" aria-label="Two colleagues talking across a glass office table"></div>
  <p class="who-text">Lorem ipsum dolor sit amet, consectetur adipiscing elit. Phasellus vitae turpis eu augue dapibus euismod at vel magna. Morbi elemen tum sem sed risus rhonc placerat. Vestibulum cursus, eros ac placerat.</p>

  <h3 class="side-heading" style="top:1251px">ALSO FIND US ON</h3>
  <div class="social" aria-label="Social networks">
    <span style="background:#3b5998"></span>
    <span style="background:#2fa9e0"></span>
    <span style="background:#1b7bb5"></span>
    <span style="background:#d5432f"></span>
    <span style="background:#c4302b"></span>
  </div>

  <div class="ad" style="top:1397px"><span>SQUARE BUTTON AD</span><span>(125X125)</span></div>
  <div class="ad" style="top:1654px"><span>SQUARE BUTTON AD</span><span>(125X125)</span></div>
  <div class="ad" style="top:1912px"><span>SQUARE BUTTON AD</span><span>(125X125)</span></div>
</aside>

<svg class="footer-wave" viewBox="0 0 1200 90" preserveAspectRatio="none" aria-hidden="true">
  <path d="M0 28 C 300 -4, 600 -4, 900 30 S 1150 50, 1200 18 L1200 90 L0 90 Z" fill="var(--gold)"/>
  <path d="M0 36 C 300 4, 600 4, 900 38 S 1150 58, 1200 26 L1200 90 L0 90 Z" fill="var(--green)"/>
  <path d="M0 42 C 300 10, 600 10, 900 44 S 1150 64, 1200 32 L1200 90 L0 90 Z" fill="var(--black)"/>
</svg>

<footer class="footer">
  <div class="footer-brand">
    <span class="brand-mark"></span>
    <span class="brand-name">HARBORLINE<br>TRADE PARTNERS</span>
  </div>
  <div class="footer-name">Harborline Trade Partners</div>
  <div class="footer-line footer-address">
    <svg viewBox="0 0 24 24"><path d="M12 2a7 7 0 0 0-7 7c0 5 7 13 7 13s7-8 7-13a7 7 0 0 0-7-7zm0 9.5A2.5 2.5 0 1 1 12 6.5a2.5 2.5 0 0 1 0 5z"/></svg>
    <span>418 Quayside Avenue, Port Elden, OR 97410</span>
  </div>
  <div class="footer-line footer-contact">
    <svg viewBox="0 0 24 24"><path d="M6.6 10.8a15 15 0 0 0 6.6 6.6l2.2-2.2a1 1 0 0 1 1-.25 11.4 11.4 0 0 0 3.6.57 1 1 0 0 1 1 1V20a1 1 0 0 1-1 1A17 17 0 0 1 3 4a1 1 0 0 1 1-1h3.5a1 1 0 0 1 1 1c0 1.25.2 2.45.57 3.57a1 1 0 0 1-.25 1z"/></svg>
    <span>555-014-2290</span><span class="sep">|</span>
    <svg viewBox="0 0 24 24"><path d="M2 5h20v14H2z M2 5l10 8 10-8" stroke="#000" stroke-width="1.5"/></svg>
    <a href="#">info@harborlinetrade.com</a><span class="sep">|</span>
    <svg viewBox="0 0 24 24"><path d="M10 14a4 4 0 0 0 5.7 0l3.5-3.5a4 4 0 0 0-5.7-5.7l-1.2 1.2 1.4 1.4 1.2-1.2a2 2 0 0 1 2.9 2.9l-3.5 3.5a2 2 0 0 1-2.9 0zm4-4a4 4 0 0 0-5.7 0l-3.5 3.5a4 4 0 0 0 5.7 5.7l1.2-1.2-1.4-1.4-1.2 1.2a2 2 0 0 1-2.9-2.9l3.5-3.5a2 2 0 0 1 2.9 0z"/></svg>
    <a href="#">harborlinetrade.com</a>
  </div>
  <div class="copyright">©2014 Harborline Trade Partners.</div>
</footer>

</body>
</html>
```